Kelvane Plumbing Business cards

Company is Kelvane Plumbing.
name Dashel Morrowby, I am a plumber, drainer, gasfitter and roofer
Mobile: 0431 906 154
Email address: info@kelvaneplumbing.example (check out my website for some ideas)
Website: www.kelvaneplumbing.example
ABN: 82 916 203 471
LIC: 604517K

I am reliable all round plumber. I am a 24 hour emergency service. Kelvane Plumbing is a professional plumbing service in the Illawarra, South Coast, Southern Sydney and Southern Highland regions of NSW. We offer a 24 hour emergency service for piece of mind to our customers. Call us now to see how we can help you. Kelvane Plumbing approaches every job with attention to detail and excellent customer service. With our superior workmanship you can be confident that the job will be done right the first time around. You can rest assured with results that are guaranteed to last.

Target Market(s)

the general public

Contact Information for Business Card

look up website for some ideas something with similar colours to logo and new modern and to catch the eye.

Colors
fdfdfd
ffffff
000000
7f7f7f
aaaaaa
33a6d7
0492cd

Requirements
Must have
• all contact details
• company- Kelvane Plumbing
• name- Dashel Morrowby
• number mobile- 0431 906 154
• Email address- info@kelvaneplumbing.example
• Website- www.kelvaneplumbing.example
• ABN- 82 916 203 471
• LIC- 604517K

```html
<!DOCTYPE html>
<html lang="en">
<head>
<meta charset="utf-8">
<title>Kelvane Plumbing – Business Cards</title>
<link rel="stylesheet" href="https://fonts.googleapis.com/css2?family=Arimo:wght@400;700&family=Noto+Serif:wght@400&family=Nunito+Sans:wght@400;600&display=swap">
<style>
  :root {
    --page: #fdfdfd;
    --card-grey: #e9e9ea;
    --brand-blue: #049bcb;
    --ink-blue: #0492cd;
    --icon-ink: #1a1a1a;
    --white: #ffffff;
    --watermark: #c2d6e3;
    --divider: #b8b8b8;
  }
  html, body {
    margin: 0;
    padding: 0;
    width: 1200px;
    height: 1200px;
    overflow: hidden;
    background: var(--page);
  }
  .canvas {
    position: relative;
    width: 1200px;
    height: 1200px;
  }
  .card {
    position: absolute;
    left: 194px;
    width: 840px;
    height: 480px;
    overflow: hidden;
    background: var(--card-grey);
  }
  .card--front { top: 89px; }
  .card--back {
    top: 581px;
    border-top: 1px solid var(--divider);
  }
  .card__band {
    position: absolute;
    left: 0;
    right: 0;
    bottom: 0;
    background: var(--brand-blue);
  }
  .card--front .card__band { top: 269px; }
  .card--back .card__band { top: 265px; }

  .brand-name {
    position: absolute;
    left: 0;
    right: 0;
    top: 196px;
    margin: 0;
    text-align: center;
    font-family: "Arimo", Arial, sans-serif;
    font-weight: 700;
    font-size: 60px;
    letter-spacing: 1px;
    color: var(--ink-blue);
    line-height: 1;
  }

  .tool-artwork {
    position: absolute;
    left: 558px;
    top: 86px;
    width: 282px;
    height: 179px;
    background: linear-gradient(135deg, rgba(194,214,227,0.2), var(--watermark) 60%);
    border-radius: 40px 40px 0 0;
    opacity: 0.75;
  }

  .holder {
    position: absolute;
    left: 0;
    right: 0;
    top: 106px;
    text-align: center;
  }
  .holder__name {
    margin: 0 0 0 4px;
    font-family: "Arimo", Arial, sans-serif;
    font-weight: 400;
    font-size: 56px;
    line-height: 1;
    color: var(--ink-blue);
  }
  .holder__role {
    margin: 10px 0 0 0;
    font-family: "Noto Serif", Georgia, serif;
    font-size: 19px;
    letter-spacing: 0.6px;
    color: var(--ink-blue);
  }

  .contact-list {
    position: absolute;
    left: 42px;
    top: 290px;
    margin: 0;
    padding: 0;
    list-style: none;
  }
  .contact-list__item {
    display: flex;
    align-items: center;
    height: 30px;
    margin-bottom: 16px;
    font-family: "Nunito Sans", Arial, sans-serif;
    font-size: 16px;
    letter-spacing: 0.4px;
    color: var(--white);
  }
  .contact-list__icon {
    width: 32px;
    height: 30px;
    margin-right: 20px;
    flex: none;
  }
  .registration {
    position: absolute;
    right: 28px;
    top: 410px;
    font-family: "Nunito Sans", Arial, sans-serif;
    font-size: 13px;
    letter-spacing: 0.3px;
    color: var(--white);
  }
</style>
</head>
<body>
<main class="canvas">

  <section class="card card--front" aria-label="Card front">
    <div class="card__band"></div>
    <h1 class="brand-name">Kelvane Plumbing</h1>
  </section>

  <section class="card card--back" aria-label="Card back">
    <div class="tool-artwork" role="img" aria-label="Faint illustration of two crossed pipe wrenches"></div>
    <div class="card__band"></div>

    <div class="holder">
      <h2 class="holder__name">Dashel Morrowby</h2>
      <p class="holder__role">Plumber, drainer, gasfitter and roofer</p>
    </div>

    <ul class="contact-list">
      <li class="contact-list__item">
        <svg class="contact-list__icon" viewBox="0 0 32 30" aria-hidden="true">
          <path fill="var(--icon-ink)" d="M7 3c1.5-1 3-.6 3.8.8l2.4 4.2c.6 1.1.3 2.3-.7 3l-1.8 1.2c1.2 3 3.6 5.6 6.6 7l1.3-1.7c.8-1 2-1.2 3.1-.6l4.2 2.5c1.3.8 1.6 2.4.7 3.7l-1.6 2.2c-1 1.3-2.7 1.9-4.3 1.4C12.5 24.5 5.5 17.5 3.3 9.3 2.9 7.7 3.5 6 4.8 5z"/>
        </svg>
        <span>0431 906 154</span>
      </li>
      <li class="contact-list__item">
        <svg class="contact-list__icon" viewBox="0 0 32 30" aria-hidden="true">
          <rect x="2" y="6" width="28" height="18" fill="none" stroke="var(--icon-ink)" stroke-width="2.4"/>
          <path d="M2 6l14 11L30 6M2 24l10-9M30 24l-10-9" fill="none" stroke="var(--icon-ink)" stroke-width="2.4"/>
        </svg>
        <span>info@kelvaneplumbing.example</span>
      </li>
      <li class="contact-list__item">
        <svg class="contact-list__icon" viewBox="0 0 32 30" aria-hidden="true">
          <g fill="none" stroke="var(--icon-ink)" stroke-width="2">
            <circle cx="16" cy="15" r="13"/>
            <ellipse cx="16" cy="15" rx="6" ry="13"/>
            <path d="M3 15h26M5 8h22M5 22h22"/>
          </g>
        </svg>
        <span>www.kelvaneplumbing.example</span>
      </li>
    </ul>

    <p class="registration">ABN- 82 916 203 471 LIC- 604517K</p>
  </section>

</main>
</body>
</html>
```